Business card design needed

We need a business card design for a new micro business based in Melbourne (Australia). Our main service is cleaning and fixing Vertical Blinds as a cheaper alternative than buying new blinds. A smaller part of the business is fitting affordable & temporary alternatives to double glazed windows both for noise abatement and climate control and reduction in energy costs.
We could be dealing with commercial as well as residential customers so we need a quality look. The design needs to reflect our core business of vertical blinds cleaning & maintenance.

Target Market(s)

Not sure yet. These Business Cards are going to be used to test the market

Industry/Entity Type

Residential

Contact Information for Business Card

Morlena Tazwick. Vertical Blinds Cleaning, Maintenance & Temporary Window Insulation Solutions. Ph: 03 7142 5063. Mob: 0471 356 249.

```html
<!DOCTYPE html>
<html lang="en">
<head>
<meta charset="utf-8">
<title>Morlena Tazwick – Vertical Blinds</title>
<link rel="stylesheet" href="https://fonts.googleapis.com/css2?family=PT+Sans:wght@400;700&display=swap">
<style>
  :root {
    --slate: #868787;
    --lime: #a8cc3a;
    --white: #ffffff;
    --ink: #231f20;
  }
  html, body {
    margin: 0;
    padding: 0;
    width: 1200px;
    height: 693px;
    overflow: hidden;
    background: var(--slate);
  }
  .card {
    position: relative;
    width: 1200px;
    height: 693px;
    background: var(--slate);
    font-family: "PT Sans", "Myriad Pro", Arial, sans-serif;
    overflow: hidden;
  }
  .service-icon {
    position: absolute;
    top: 165px;
    width: 92px;
    height: 83px;
    background: var(--lime);
    border-radius: 12px;
  }
  .service-icon svg { width: 100%; height: 100%; display: block; }
  .icon-clean { left: 244px; }
  .icon-repair { left: 351px; }
  .icon-inspect { left: 457px; }

  .stripe-band {
    position: absolute;
    top: 269px;
    height: 124px;
  }
  .stripe-band--left {
    left: 0;
    width: 551px;
    background: repeating-linear-gradient(90deg, var(--lime) 0 37.5px, var(--white) 37.5px 46.9px);
  }
  .stripe-band--right {
    left: 974px;
    width: 226px;
    background: repeating-linear-gradient(90deg, var(--lime) 0 39px, var(--white) 39px 47.5px);
  }
  .name-panel {
    position: absolute;
    top: 269px;
    left: 551px;
    width: 423px;
    height: 124px;
    background: var(--white);
    color: var(--ink);
  }
  .name {
    position: absolute;
    left: 20px;
    top: 4px;
    margin: 0;
    font-size: 46px;
    font-weight: 700;
    line-height: 56px;
    white-space: nowrap;
  }
  .contact {
    position: absolute;
    left: 21px;
    margin: 0;
    font-size: 26px;
    line-height: 30px;
    white-space: nowrap;
  }
  .contact--phone { top: 58px; }
  .contact--mobile { top: 90px; }

  .service-line {
    position: absolute;
    right: 0;
    height: 39px;
    display: flex;
    align-items: center;
    white-space: nowrap;
  }
  .service-line--blinds { top: 413px; left: 564px; }
  .service-line--window { top: 472px; left: 566px; }
  .service-title {
    color: var(--lime);
    font-weight: 700;
    font-size: 26px;
    padding-right: 6px;
  }
  .service-detail {
    flex: 1;
    align-self: stretch;
    display: flex;
    align-items: center;
    background: var(--white);
    color: var(--ink);
    font-size: 26px;
    padding-left: 7px;
  }
</style>
</head>
<body>
<div class="card">
  <div class="service-icon icon-clean">
    <svg viewBox="0 0 92 83" aria-hidden="true">
      <g fill="var(--slate)">
        <rect x="30" y="9" width="26" height="8" rx="2"/>
        <rect x="36" y="17" width="12" height="9"/>
        <path d="M36 26 H48 L58 46 Q62 56 60 66 Q59 74 52 74 H32 Q25 74 24 66 Q22 56 26 46 Z"/>
        <rect x="61" y="7" width="3" height="3"/>
        <rect x="66" y="11" width="6" height="2"/>
        <rect x="66" y="15" width="6" height="2"/>
        <rect x="61" y="17" width="3" height="3"/>
      </g>
    </svg>
  </div>
  <div class="service-icon icon-repair">
    <svg viewBox="0 0 92 83" aria-hidden="true">
      <g fill="var(--slate)">
        <path d="M18 20 A14 14 0 0 0 38 36 L64 68 Q68 73 73 69 Q77 65 72 61 L42 31 A14 14 0 0 0 26 12 L34 21 L28 27 Z"/>
      </g>
    </svg>
  </div>
  <div class="service-icon icon-inspect">
    <svg viewBox="0 0 92 83" aria-hidden="true">
      <circle cx="38" cy="35" r="17" fill="none" stroke="var(--slate)" stroke-width="6"/>
      <line x1="51" y1="48" x2="70" y2="67" stroke="var(--slate)" stroke-width="9" stroke-linecap="round"/>
    </svg>
  </div>

  <div class="stripe-band stripe-band--left"></div>
  <div class="stripe-band stripe-band--right"></div>

  <div class="name-panel">
    <h1 class="name">Morlena Tazwick</h1>
    <p class="contact contact--phone">Ph: 03 7142 5063</p>
    <p class="contact contact--mobile">Mob: 0471 356 249</p>
  </div>

  <div class="service-line service-line--blinds">
    <span class="service-title">Vertical Blinds</span>
    <span class="service-detail">Cleaning, Maintenance</span>
  </div>
  <div class="service-line service-line--window">
    <span class="service-title">Temporary Window</span>
    <span class="service-detail">Insulation Solutions</span>
  </div>
</div>
</body>
</html>
```